Online Consultancy Needs a New Logo & Business Card Design

Based on the new logo we just received from another contest here on Maketrove,

You'll find a few different versions of our logo as well as examples of business card designs we like in this folder:
==> https://share.plumvault.net/folderview?id=7Kq2WzTn4pLrXcv9BsHaYe1MoD5g&usp=sharing

We are considering two options:
- clean, black design
- clean, white/blue design

We're willing to consider both options.

We're considering adding some special effects to the cards when printing - emboss, rounded corners, etc.

However, please deliver a design WITHOUT round corners.

Target Market(s)

Successful business people, serious and older audience.

Industry/Entity Type

Business

Contact Information for Business Card

For the business card, I would like a minimalistic card with the logo on one side (perhaps in the middle) and the contact information on the other.

For the contact information please use:
Name: Peter Lund
Position: Founder
Email: peter.lund@korvim.com
Phone Number: +381 63 98 76 210
Website URL: www.korvim.com

Font styles to use
Serif
Sans Serif

Requirements
Must have
• Must fit in perfectly with our current website design.

```html
<!DOCTYPE html>
<html lang="en">
<head>
<meta charset="utf-8">
<title>Korvim Business Card</title>
<link rel="stylesheet" href="https://fonts.googleapis.com/css2?family=Open+Sans:wght@300;400;600&display=swap">
<style>
  :root {
    --page-bg: #ece7df;
    --card-blue: #3ea6d3;
    --card-blue-deep: #2a8fc0;
    --ornament-blue: #2f8fbf;
    --ink-dark: #16242f;
    --band-black: #0b0b0c;
    --text-light: #f2f6f8;
    --accent-blue: #41b4e8;
    --back-frame: #0a0a0a;
    --back-panel: #2a2d30;
    --back-panel-dark: #1f2225;
  }
  * { margin: 0; padding: 0; box-sizing: border-box; }
  html, body {
    width: 1200px; height: 970px; overflow: hidden;
    background: var(--page-bg);
    font-family: "Open Sans", Arial, sans-serif;
  }
  .canvas { position: relative; width: 1200px; height: 970px; }

  .card-front {
    position: absolute; left: 155px; top: 20px; width: 371px; height: 922px;
    background: linear-gradient(180deg, var(--card-blue) 0%, var(--card-blue-deep) 100%);
    overflow: hidden;
  }
  .front-ornament {
    position: absolute; left: 120px; top: 0; width: 251px; height: 772px;
    background: radial-gradient(ellipse at 60% 20%, rgba(47,143,191,0.55) 0%, rgba(47,143,191,0) 70%);
  }
  .holder-name {
    position: absolute; top: 180px; width: 100%; text-align: center;
    font-weight: 400; font-size: 54px; color: var(--ink-dark); letter-spacing: 0.5px;
  }
  .name-rule {
    position: absolute; left: 35px; top: 262px; width: 301px; height: 2px;
    background: var(--ink-dark); opacity: 0.55;
  }
  .holder-title {
    position: absolute; top: 298px; width: 100%; text-align: center;
    font-weight: 400; font-size: 39px; color: var(--ink-dark);
  }
  .web-band {
    position: absolute; left: 0; top: 381px; width: 100%; height: 65px;
    background: var(--band-black); color: var(--text-light);
    font-size: 40px; line-height: 65px; text-align: center;
  }
  .contact-band {
    position: absolute; left: 0; top: 772px; width: 100%; height: 150px;
    background: var(--band-black); color: var(--text-light);
  }
  .contact-phone {
    position: absolute; top: 30px; width: 100%;
    display: flex; justify-content: center; align-items: center; gap: 12px;
    font-size: 31px;
  }
  .contact-phone svg { width: 24px; height: 40px; }
  .contact-email {
    position: absolute; top: 96px; width: 100%; text-align: center; font-size: 29px;
  }

  .card-back {
    position: absolute; left: 676px; top: 20px; width: 364px; height: 922px;
    background: var(--back-frame);
  }
  .back-panel {
    position: absolute; left: 20px; top: 20px; right: 20px; bottom: 20px;
    background: radial-gradient(ellipse at 50% 45%, var(--back-panel) 0%, var(--back-panel-dark) 100%);
  }
  .brand-lockup {
    position: absolute; left: 43px; top: 383px; width: 296px; height: 93px;
    border-radius: 47px; background: var(--back-frame);
    display: flex; align-items: center; justify-content: center; gap: 16px;
    color: var(--accent-blue); font-weight: 600; font-size: 50px; letter-spacing: 1px;
  }
  .brand-dot { width: 26px; height: 26px; border-radius: 50%; background: var(--accent-blue); }
</style>
</head>
<body>
<main class="canvas">
  <section class="card-front">
    <div class="front-ornament" role="img" aria-label="Floral swirl ornament in deeper blue"></div>
    <h1 class="holder-name">Peter Lund</h1>
    <div class="name-rule"></div>
    <p class="holder-title">Founder</p>
    <div class="web-band">www.korvim.com</div>
    <div class="contact-band">
      <p class="contact-phone">
        <svg viewBox="0 0 24 40" aria-hidden="true">
          <rect x="2" y="2" width="20" height="36" rx="4" fill="#41b4e8"/>
          <rect x="5" y="7" width="14" height="20" fill="#0b0b0c"/>
          <circle cx="12" cy="32" r="2.5" fill="#0b0b0c"/>
        </svg>
        <span>+381 63 98 76 210</span>
      </p>
      <p class="contact-email">peter.lund@korvim.com</p>
    </div>
  </section>

  <section class="card-back">
    <div class="back-panel"></div>
    <div class="brand-lockup">
      <span class="brand-dot"></span>
      <span class="brand-name">korvim</span>
    </div>
  </section>
</main>
</body>
</html>
```